Food broker, trader, wholesaler, liquidator looking for a 5 pages website

Looking for a 5 pages website design. We are food brokers, traders, wholesaler and closeout buyer working with manufacturers, distributors, importers sell to retailers, food service operators and industrial (ingredients). We help market their products. We are a resource for those who need a solution in the distribution/selling/placement of food on the shelves, kitchens and pantries. Whether we open new accounts with new products or sell short dated inventory, we know where to go and get results.

Target Market(s)

Food manufacturers, food distributors, food brokers

Coding

Coded - Design and coding required

Number of Pages Required

4 page

Font styles to use
Serif

Requirements
Must have
• Food-food production-warehouse-Food packaging-people meeting-trucks-supermarket shelves-

```html
<!DOCTYPE html>
<html lang="en">
<head>
<meta charset="utf-8">
<title>Larderline Merchant</title>
<link href="https://fonts.googleapis.com/css2?family=Noticia+Text:wght@400;700&family=Mulish:wght@400;600&display=swap" rel="stylesheet">
<style>
:root{
  --navy:#101a6e;
  --navy-deep:#0c1866;
  --ink:#333a45;
  --muted:#666b73;
  --line:#d9dbe0;
  --footer:#2c2c2c;
  --footer-line:#444;
  --white:#ffffff;
}
*{margin:0;padding:0;box-sizing:border-box}
html,body{width:1200px;height:3617px;overflow:hidden}
body{position:relative;background:var(--white);font-family:"Noticia Text",Georgia,serif;color:var(--ink)}
.abs{position:absolute}

/* header */
.site-header{position:absolute;left:0;top:0;width:1200px;height:115px;background:var(--white);border-bottom:1px solid #e4e4e4}
.brand{position:absolute;left:112px;top:30px;display:flex;align-items:center;gap:10px;font-weight:700;font-size:21px;color:var(--navy);letter-spacing:.3px}
.brand-dot{width:26px;height:26px;background:var(--navy);border-radius:50%}
.main-nav{position:absolute;top:46px;left:584px;display:flex;gap:45px;font-size:14px;color:#333}
.main-nav a{color:inherit;text-decoration:none}
.main-nav .active{color:var(--navy)}

/* hero */
.hero{position:absolute;left:0;top:115px;width:1200px;height:685px;background:linear-gradient(180deg,#d9b642 0%,#b38d4c 22%,#8f8a86 48%,#b0b2b5 75%,#cfd0d2 100%)}
.hero-panel{position:absolute;left:337px;top:292px;width:505px;height:269px;background:rgba(70,70,75,.45);text-align:center;color:var(--white)}
.hero-panel h1{font-weight:400;font-size:48px;margin-top:20px}
.hero-panel p{font-size:17px;line-height:37px;margin-top:6px}
.btn-solid{display:inline-block;background:var(--navy);color:var(--white);font-size:15px;border-radius:3px;text-decoration:none}
.hero .btn-solid{margin-top:14px;padding:14px 24px}
.dots{position:absolute;left:577px;top:660px;display:flex;gap:9px}
.dots span{width:10px;height:10px;border-radius:50%;background:#777}
.dots .on{background:var(--navy)}

/* headings */
.section-title{position:absolute;left:0;width:1200px;text-align:center;font-weight:400;font-size:40px;color:var(--navy)}
.section-sub{position:absolute;left:0;width:1200px;text-align:center;font-size:15.5px;color:#555}

/* process */
.process{position:absolute;left:0;top:800px;width:1200px;height:863px}
.step-label{position:absolute;font-size:19px;line-height:34px;color:#333}

/* about */
.about{position:absolute;left:0;top:1663px;width:1200px;height:484px}
.about-copy{position:absolute;left:0;top:0;width:682px;height:484px;background:var(--navy-deep);color:var(--white)}
.about-copy h2{position:absolute;left:139px;top:72px;font-weight:400;font-size:46px}
.about-rule{position:absolute;left:139px;top:136px;width:60px;height:3px;background:var(--white)}
.about-copy p{position:absolute;left:139px;top:170px;width:468px;font-size:12.5px;line-height:30px;text-align:justify}
.btn-outline{position:absolute;left:139px;top:376px;width:131px;height:48px;border:1px solid var(--white);border-radius:3px;color:var(--white);font-size:14px;line-height:46px;text-align:center;text-decoration:none}
.about-photo{position:absolute;left:682px;top:0;width:518px;height:484px;background:linear-gradient(135deg,#c9c6bf 0%,#a8a59e 40%,#8aa0c2 70%,#d4cfc4 100%)}

/* services */
.service-card{position:absolute;top:2312px;width:309px;height:390px;border:1px solid #e3e3e3;box-shadow:0 0 4px rgba(0,0,0,.06);text-align:center;background:var(--white)}
.service-photo{position:absolute;left:10px;top:9px;width:289px;height:214px}
.service-card h3{position:absolute;left:0;top:248px;width:100%;font-weight:400;font-size:19.5px;color:#333}
.service-rule{position:absolute;left:133px;top:288px;width:42px;height:2px;background:var(--navy)}
.service-card p{position:absolute;left:20px;top:304px;width:269px;font-family:"Mulish",Arial,sans-serif;font-size:13px;line-height:25px;color:var(--muted)}

/* contact */
.contact{position:absolute;left:0;top:2762px;width:1200px;height:480px;background:linear-gradient(180deg,#f1f2f4 0%,#eceef1 60%,#e6e6e6 100%)}
.field{position:absolute;background:var(--white);border:1px solid #d5d7dc;font-size:13px;color:#666;padding:0 16px;line-height:44px}
.field-message{line-height:20px;padding-top:14px}
.contact .btn-solid{position:absolute;left:526px;top:382px;width:149px;height:48px;line-height:48px;text-align:center;border-radius:0;font-size:14px}

/* footer */
.site-footer{position:absolute;left:0;top:3242px;width:1200px;height:375px;background:var(--footer);color:var(--white);font-family:"Mulish",Arial,sans-serif}
.footer-brand{position:absolute;left:130px;top:185px;width:242px;text-align:center;font-family:"Noticia Text",Georgia,serif;font-weight:700;font-size:20px}
.footer-brand .brand-dot{display:block;margin:0 auto 16px;width:40px;height:40px;background:var(--white)}
.footer-col h4{position:absolute;top:46px;font-family:"Noticia Text",Georgia,serif;font-weight:400;font-size:24px}
.footer-list{position:absolute;top:100px;list-style:none;font-size:14.5px}
.footer-list li{height:35px;padding-left:27px;position:relative}
.footer-list li::before{content:"»";position:absolute;left:2px;top:-2px}
.newsletter-text{position:absolute;left:836px;top:100px;width:260px;font-size:14px;line-height:25px}
.newsletter-field{position:absolute;left:836px;top:169px;width:250px;height:42px;background:var(--white);color:#555;font-size:13px;line-height:42px;padding-left:14px}
.newsletter-btn{position:absolute;left:836px;top:218px;width:96px;height:37px;background:var(--navy);font-size:14px;line-height:37px;text-align:center}
.footer-rule{position:absolute;left:112px;top:298px;width:976px;height:1px;background:var(--footer-line)}
.copyright{position:absolute;left:0;top:326px;width:1200px;text-align:center;font-size:13.5px}
</style>
</head>
<body>

<header class="site-header">
  <div class="brand"><span class="brand-dot"></span>LARDERLINE MERCHANT</div>
  <nav class="main-nav">
    <a class="active" href="#">Home</a>
    <a href="#">About Us</a>
    <a href="#">What we do</a>
    <a href="#">Contact</a>
    <a href="#">Giving Back</a>
  </nav>
</header>

<section class="hero" role="img" aria-label="Supermarket aisle with fully stocked shelves of canned and packaged food">
  <div class="hero-panel">
    <h1>Larderline Merchant</h1>
    <p>Sed ut perspiciatis unde omnis iste natus error sit<br>voluptatem accusantium doloremque laudantium,<br>totam rem aperiam</p>
    <a class="btn-solid" href="#">Read More</a>
  </div>
  <div class="dots"><span></span><span class="on"></span><span></span></div>
</section>

<section class="process">
  <h2 class="section-title" style="top:44px">Our Process</h2>
  <p class="section-sub" style="top:113px">Sed ut perspiciatis unde omnis iste natus error sit voluptatem accusantium doloremque</p>

  <svg class="abs" style="left:0;top:0" width="1200" height="863" viewBox="0 0 1200 863" fill="none" stroke="#101a6e">
    <defs>
      <marker id="arrowhead" viewBox="0 0 12 12" refX="10" refY="6" markerWidth="12" markerHeight="12" orient="auto">
        <path d="M1 1 L11 6 L1 11 L4 6 Z" fill="#fff" stroke="#101a6e" stroke-width="1.3"/>
      </marker>
    </defs>
    <g stroke-width="3.2" marker-end="url(#arrowhead)">
      <path d="M622 243 Q680 245 724 270"/>
      <path d="M822 358 Q850 400 861 453"/>
      <path d="M860 597 Q850 640 810 680"/>
      <path d="M708 760 Q650 785 563 787"/>
      <path d="M446 733 Q405 705 378 680"/>
      <path d="M331 560 Q327 490 334 435"/>
      <path d="M405 325 Q445 285 498 263"/>
    </g>
    <g stroke-width="2" fill="#fff">
      <circle cx="557" cy="250" r="54"/>
      <circle cx="770" cy="316" r="54"/>
      <circle cx="858" cy="523" r="54"/>
      <circle cx="762" cy="723" r="54"/>
      <circle cx="505" cy="765" r="54"/>
      <circle cx="344" cy="616" r="54"/>
      <circle cx="363" cy="376" r="54"/>
    </g>
    <g stroke-width="2">
      <!-- production machine -->
      <rect x="535" y="232" width="44" height="28" rx="2"/><circle cx="566" cy="246" r="7"/><path d="M541 240h12M541 248h12M550 260v12M544 272h26"/>
      <!-- warehouse -->
      <path d="M746 312 L770 296 L794 312 V338 H746 Z"/><rect x="757" y="318" width="26" height="20"/><path d="M757 326h26M757 332h26"/>
      <!-- packaging jar -->
      <rect x="840" y="507" width="36" height="38" rx="3"/><rect x="843" y="499" width="30" height="8"/><path d="M848 526 q10-8 18 0 q-8 8-18 0 Z M866 526 l6-5v10z"/>
      <!-- people -->
      <circle cx="750" cy="709" r="7"/><circle cx="774" cy="709" r="7"/><circle cx="762" cy="702" r="8"/><path d="M738 742 v-16 q12-10 24-2 q12-8 24 2 v16 Z"/>
      <!-- truck -->
      <rect x="478" y="748" width="32" height="26"/><path d="M510 756 h14 l8 10 v8 h-22"/><circle cx="489" cy="778" r="5"/><circle cx="523" cy="778" r="5"/>
      <!-- shelves -->
      <rect x="318" y="594" width="52" height="44"/><path d="M318 609h52M318 624h52M326 594v-6M340 594v-8M354 594v-6M330 609v-10M348 624v-10"/>
      <!-- bowl of food -->
      <path d="M336 378 h54 q-4 18-27 18 q-23 0-27-18 Z"/><path d="M345 378 q18-22 36 0 M352 378 q11-12 22 0 M356 360 q4-8 0-14 M364 358 q4-8 0-14 M372 360 q4-8 0-14"/>
    </g>
    <circle cx="587" cy="484" r="38" fill="#101a6e" stroke="none"/>
  </svg>
  <div class="abs" style="left:480px;top:536px;width:214px;text-align:center;font-weight:700;font-size:18px;color:var(--navy)">Larderline Merchant</div>

  <div class="step-label" style="left:394px;top:178px">Food<br>Production</div>
  <div class="step-label" style="left:842px;top:293px">Warehouse</div>
  <div class="step-label" style="left:927px;top:485px">Food<br>Packaging</div>
  <div class="step-label" style="left:834px;top:698px">People<br>Meeting</div>
  <div class="step-label" style="left:378px;top:763px">Trucks</div>
  <div class="step-label" style="left:153px;top:592px">Supermarket<br>Shelves</div>
  <div class="step-label" style="left:245px;top:354px">Food</div>
</section>

<section class="about">
  <div class="about-copy">
    <h2>About Us</h2>
    <div class="about-rule"></div>
    <p>Larderline Merchant works with food manufacturers, brand owners, distributors and wholesalers market their products. Retail, Food Service and Industrial ingredients.Founded in 2008, Larderline Merchant started with the distribution of gluten free products understanding the need to provide access to unique flavors and products forthe celiac consumers. From this, we expanded into deli, dairy, groceries, frozen and beverages.</p>
    <a class="btn-outline" href="#">READ MORE</a>
  </div>
  <div class="about-photo" role="img" aria-label="Smiling warehouse manager holding a clipboard between tall storage racks"></div>
</section>

<h2 class="section-title" style="top:2190px">What We Do</h2>
<p class="section-sub" style="top:2252px">Sed ut perspiciatis unde omnis iste natus error sit voluptatem accusantium doloremque</p>

<article class="service-card" style="left:112px">
  <div class="service-photo" role="img" aria-label="Sales team meeting in an office with market charts on screens" style="background:linear-gradient(135deg,#2c3442,#5a6577 55%,#c9ccd1)"></div>
  <h3>Sales &amp; Marketing</h3>
  <div class="service-rule"></div>
  <p>we connect food buyers and sellers through a dedicated approach.</p>
</article>
<article class="service-card" style="left:445px">
  <div class="service-photo" role="img" aria-label="Hands typing on a laptop in front of trading screens" style="background:linear-gradient(135deg,#3a4a5c,#6f7c88 50%,#b89a6e)"></div>
  <h3>Trading</h3>
  <div class="service-rule"></div>
  <p>we purchase goods anywhere and ship them Nationwide and Export.</p>
</article>
<article class="service-card" style="left:779px">
  <div class="service-photo" role="img" aria-label="Warehouse aisle with pallets of boxed inventory and a forklift" style="background:linear-gradient(135deg,#b9a68a,#c98f52 45%,#7c8fb0)"></div>
  <h3>Closeout/Excess Inventory</h3>
  <div class="service-rule"></div>
  <p>we buy closeouts and excess inventory for prisons, outlet stores and discounters.</p>
</article>

<section class="contact" role="img" aria-label="Faint warehouse backdrop behind the contact form">
  <h2 class="section-title" style="top:50px">Contact Us</h2>
  <p class="section-sub" style="top:110px">Sed ut perspiciatis unde omnis iste natus error sit voluptatem accusantium</p>
  <div class="field" style="left:281px;top:161px;width:314px;height:44px">First Name :</div>
  <div class="field" style="left:606px;top:161px;width:313px;height:44px">Last Name :</div>
  <div class="field" style="left:281px;top:218px;width:314px;height:43px">Email :</div>
  <div class="field" style="left:606px;top:218px;width:313px;height:43px">Phone :</div>
  <div class="field field-message" style="left:281px;top:274px;width:638px;height:85px">Message :</div>
  <a class="btn-solid" href="#">SUBMIT</a>
</section>

<footer class="site-footer">
  <div class="footer-brand"><span class="brand-dot"></span>LARDERLINE MERCHANT</div>
  <div class="footer-col"><h4 style="left:396px">Quick Links</h4></div>
  <ul class="footer-list" style="left:396px">
    <li>Home</li><li>About Us</li><li>What we do</li><li>Contact</li><li>Giving Back</li>
  </ul>
  <div class="footer-col"><h4 style="left:612px">Services</h4></div>
  <ul class="footer-list" style="left:612px">
    <li>Sed ut perspiciatis</li><li>unde omnis iste</li><li>natus error sit</li><li>voluptatem</li><li>accusantium</li>
  </ul>
  <div class="footer-col"><h4 style="left:836px">Newsletter</h4></div>
  <p class="newsletter-text">Sed ut perspiciatis unde omnis iste natus error sit voluptatem</p>
  <div class="newsletter-field">Email :</div>
  <div class="newsletter-btn">SUBMIT</div>
  <div class="footer-rule"></div>
  <p class="copyright">© Copyright 2020 Larderline Merchant.All Rights Reserved</p>
</footer>

</body>
</html>
```